App Redesign for PathMentor

We're looking for a skilled UI/UX designer to modernize the PathMentor mobile app, enhancing user engagement while preserving our current brand identity.

Key Objectives:
Refresh the app using modern design trends
Maintain a clean, calm, and playful aesthetic aligned with our brand
Boost engagement through improved flow, visuals, and interactivity

Design Requirements:
Retain recognizability from our app and website (see Brand ID Guide) (and website pathmentorhub.example)
Reflect a tone that is supportive, fun/ playful, and professional

Design 5–8 key screens, including:
Home/Dashboard
Daily Intentions Interface
Gamification Overview (Streaks, Rewards)
Social Features (Direct Realtime Feedback, Messaging, Challenges)
Progress Tracking

New Feature Concepts to Include:
Daily Intentions with voice/text input and visual encouragement
Gamification elements like streaks, badges, and animations
Social Connections including messaging, reactions, and feedback tools
Optional: Subtle design cues for future AI-driven interactions

Audience: Adults aged 25–55 interested in personal development and coaching. Tech-comfortable but not tech-savvy.

Visual Inspiration: Wordivo (gamification), Calmnest (intentions), Runqo (social support)

Target Market(s)

Corporate Leaders and Entrepreneurs

Industry/Entity Type

Leadership Training & Consultancies

Font styles to use
Sans Serif
Other font styles liked:
• Avenir, Arial

Colors
FFF300
FFF600
FEFA6F
FFFEC7
FFFEE8

Requirements
Nice to have
• Wordivo, Calmnest,

```html
<!DOCTYPE html>
<html lang="en">
<head>
<meta charset="utf-8">
<title>PeakSense Tracker</title>
<link rel="stylesheet" href="https://fonts.googleapis.com/css2?family=Inter:wght@400;500;600;700&display=swap">
<style>
  :root {
    --ink: #2f2f2f;
    --black: #0d0d0d;
    --field: #e8e9eb;
    --yellow: #fdf30b;
    --yellow-icon: #e2d800;
    --panel: #f5f5f5;
    --panel-line: #d8e0ee;
    --grid: #bdbdbd;
    --axis: #9a9a9a;
    --area-dark: #cecece;
    --area-yellow: #d7d471;
    --line-yellow: #e4dc00;
    --alert: #ff1a1a;
    --white: #ffffff;
  }
  * { box-sizing: border-box; margin: 0; padding: 0; }
  html, body { width: 1200px; height: 2541px; overflow: hidden; }
  body { background: #ececec; font-family: "Inter", Arial, sans-serif; color: var(--ink); }
  .app { position: absolute; left: 9px; top: 0; width: 1182px; height: 2541px; background: var(--white); overflow: hidden; }
  .app-title { position: absolute; left: 42px; top: 122px; font-size: 80px; font-weight: 700; letter-spacing: -1px; color: var(--ink); }
  .app-title sup { font-size: 36px; vertical-align: 36px; }
  .select { position: absolute; left: 42px; width: 1096px; height: 130px; border-radius: 65px; background: var(--field); display: flex; align-items: center; color: var(--black); font-size: 35px; }
  .select::after { content: ""; position: absolute; right: 36px; top: 58px; border-left: 14px solid transparent; border-right: 14px solid transparent; border-top: 14px solid #2c2c2c; }
  .select-stats { top: 282px; padding-left: 31px; font-weight: 600; }
  .select-listing { top: 454px; padding-left: 42px; font-weight: 500; }
  .stat-card { position: absolute; top: 640px; width: 252px; height: 390px; border-radius: 26px; background: var(--yellow); padding: 36px 0 0 36px; color: #222; }
  .stat-value { font-size: 46px; line-height: 1.1; }
  .stat-label { font-size: 31px; line-height: 1.5; margin-top: 12px; }
  .stat-icon { position: absolute; left: 28px; bottom: 18px; width: 90px; height: 90px; }
  .progress-panel { position: absolute; left: 42px; top: 1089px; width: 1096px; height: 1500px; border: 2px solid var(--panel-line); border-radius: 22px; background: var(--panel); }
  .panel-badge { position: absolute; left: 42px; top: 42px; width: 150px; height: 93px; border-radius: 47px; background: var(--black); display: flex; align-items: center; justify-content: center; }
  .panel-title { position: absolute; left: 220px; top: 64px; font-size: 40px; font-weight: 500; color: var(--black); }
  .panel-divider { position: absolute; left: 42px; right: 42px; top: 221px; height: 2px; background: #cfcfcf; }
  .chart { position: absolute; left: 0; top: 0; }
  .bottom-nav { position: absolute; left: 0; top: 2333px; width: 1182px; height: 208px; background: #fafafa; border-top: 2px solid #e6e6e6; box-shadow: 0 -6px 18px rgba(0,0,0,0.05); }
  .nav-icon { position: absolute; top: 76px; width: 60px; height: 60px; }
  .nav-avatar { position: absolute; left: 996px; top: 66px; width: 88px; height: 88px; border-radius: 50%; background: var(--black); }
  .nav-alert { position: absolute; left: 1102px; top: 45px; width: 28px; height: 28px; border-radius: 50%; background: var(--alert); }
</style>
</head>
<body>
<main class="app">
  <h1 class="app-title">PeakSense<sup>™</sup> Tracker</h1>

  <div class="select select-stats">Stats Type</div>
  <div class="select select-listing">Filter by listing</div>

  <section class="stat-card" style="left:42px">
    <div class="stat-value">21</div>
    <div class="stat-label">Weekly<br>Reports</div>
    <svg class="stat-icon" viewBox="0 0 90 90" fill="none" stroke="var(--yellow-icon)" stroke-width="6"><rect x="6" y="10" width="78" height="70" rx="6"/><line x1="6" y1="28" x2="84" y2="28"/><line x1="18" y1="19" x2="22" y2="19"/><line x1="30" y1="19" x2="34" y2="19"/></svg>
  </section>
  <section class="stat-card" style="left:323px">
    <div class="stat-value">0</div>
    <div class="stat-label">Monthly<br>reports</div>
    <svg class="stat-icon" viewBox="0 0 90 90" fill="none" stroke="var(--yellow-icon)" stroke-width="6" stroke-linejoin="round"><path d="M8 26 L18 8 L28 26 L28 74 L18 86 L8 74 Z"/><line x1="8" y1="32" x2="28" y2="32"/><rect x="40" y="6" width="28" height="80" rx="4"/><line x1="40" y1="22" x2="52" y2="22"/><line x1="40" y1="38" x2="52" y2="38"/><line x1="40" y1="54" x2="52" y2="54"/><line x1="40" y1="70" x2="52" y2="70"/></svg>
  </section>
  <section class="stat-card" style="left:604px">
    <div class="stat-value">0</div>
    <div class="stat-label">Active<br>Promotions</div>
    <svg class="stat-icon" viewBox="0 0 90 90" fill="none" stroke="var(--yellow-icon)" stroke-width="6" stroke-linejoin="round"><path d="M46 6 L14 52 L40 52 L34 86 L70 36 L44 36 Z"/></svg>
  </section>
  <section class="stat-card" style="left:885px">
    <div class="stat-value">3,316</div>
    <div class="stat-label">Visits this<br>week</div>
    <svg class="stat-icon" viewBox="0 0 90 90" stroke="var(--yellow-icon)" stroke-width="6" stroke-linecap="round"><line x1="8" y1="38" x2="8" y2="52"/><line x1="22" y1="26" x2="22" y2="64"/><line x1="36" y1="10" x2="36" y2="80"/><line x1="50" y1="22" x2="50" y2="68"/><line x1="64" y1="32" x2="64" y2="58"/><line x1="78" y1="40" x2="78" y2="50"/></svg>
  </section>

  <section class="progress-panel">
    <div class="panel-badge">
      <svg width="46" height="46" viewBox="0 0 46 46" stroke-width="4" stroke-linecap="round"><line x1="5" y1="19" x2="5" y2="27" stroke="#fff"/><line x1="14" y1="11" x2="14" y2="35" stroke="#fff"/><line x1="23" y1="3" x2="23" y2="43" stroke="#ff6b6b"/><line x1="32" y1="11" x2="32" y2="35" stroke="#fff"/><line x1="41" y1="19" x2="41" y2="27" stroke="#fff"/></svg>
    </div>
    <h2 class="panel-title">Overall Progress</h2>
    <div class="panel-divider"></div>

    <svg class="chart" width="1096" height="1300" viewBox="0 0 1096 1300" role="img" aria-label="Line chart of daily progress from Jun 19 to Jun 25">
      <g stroke="var(--grid)" stroke-width="2" stroke-dasharray="5 5">
        <line x1="183" y1="336" x2="997" y2="336"/>
        <line x1="183" y1="499" x2="997" y2="499"/>
        <line x1="183" y1="661" x2="997" y2="661"/>
        <line x1="183" y1="824" x2="997" y2="824"/>
        <line x1="183" y1="987" x2="997" y2="987"/>
      </g>
      <g fill="var(--axis)" font-family="Inter, Arial, sans-serif" font-size="25" text-anchor="end">
        <text x="154" y="345">1250</text>
        <text x="154" y="508">1000</text>
        <text x="154" y="670">750</text>
        <text x="154" y="833">500</text>
        <text x="154" y="996">250</text>
        <text x="154" y="1158">0</text>
      </g>
      <path fill="var(--area-dark)" d="M183 474 C228 474 274 925 319 925 C364 925 409 995 454 995 C499 995 545 1017 590 1017 C635 1017 681 765 726 765 C771 765 816 947 861 947 C906 947 952 834 997 834 L997 1149 L183 1149 Z"/>
      <path fill="var(--area-yellow)" d="M183 1053 C228 1053 274 1053 319 1053 C364 1053 409 1055 454 1055 C499 1055 545 1059 590 1059 C635 1059 681 1077 726 1077 C771 1077 816 1057 861 1057 C906 1057 952 1068 997 1068 L997 1149 L183 1149 Z"/>
      <path fill="none" stroke="var(--line-yellow)" stroke-width="6" d="M183 1053 C228 1053 274 1053 319 1053 C364 1053 409 1055 454 1055 C499 1055 545 1059 590 1059 C635 1059 681 1077 726 1077 C771 1077 816 1057 861 1057 C906 1057 952 1068 997 1068"/>
      <g fill="var(--line-yellow)">
        <circle cx="183" cy="1053" r="12"/><circle cx="319" cy="1053" r="12"/><circle cx="454" cy="1055" r="12"/><circle cx="590" cy="1059" r="12"/><circle cx="726" cy="1077" r="12"/><circle cx="861" cy="1057" r="12"/><circle cx="997" cy="1068" r="12"/>
      </g>
      <path fill="none" stroke="var(--black)" stroke-width="8" d="M183 474 C228 474 274 925 319 925 C364 925 409 995 454 995 C499 995 545 1017 590 1017 C635 1017 681 765 726 765 C771 765 816 947 861 947 C906 947 952 834 997 834"/>
      <g fill="var(--black)">
        <circle cx="183" cy="474" r="13"/><circle cx="319" cy="925" r="13"/><circle cx="454" cy="995" r="13"/><circle cx="590" cy="1017" r="13"/><circle cx="726" cy="765" r="13"/><circle cx="861" cy="947" r="13"/><circle cx="997" cy="834" r="13"/>
      </g>
      <g fill="var(--axis)" font-family="Inter, Arial, sans-serif" font-size="25" text-anchor="end">
        <text transform="translate(203 1222) rotate(-20)">Jun 19</text>
        <text transform="translate(339 1222) rotate(-20)">Jun 20</text>
        <text transform="translate(474 1222) rotate(-20)">Jun 21</text>
        <text transform="translate(610 1222) rotate(-20)">Jun 22</text>
        <text transform="translate(746 1222) rotate(-20)">Jun 23</text>
        <text transform="translate(881 1222) rotate(-20)">Jun 24</text>
        <text transform="translate(1017 1222) rotate(-20)">Jun 25</text>
      </g>
    </svg>
  </section>

  <nav class="bottom-nav">
    <svg class="nav-icon" style="left:74px" viewBox="0 0 60 60" fill="var(--black)"><path d="M30 6 L56 30 L48 30 L48 54 L36 54 L36 38 L24 38 L24 54 L12 54 L12 30 L4 30 Z"/></svg>
    <svg class="nav-icon" style="left:245px" viewBox="0 0 60 60" fill="none" stroke="var(--black)" stroke-width="4" stroke-linecap="round"><circle cx="22" cy="20" r="8" fill="var(--black)"/><g stroke-width="5"><line x1="22" y1="4" x2="22" y2="9"/><line x1="22" y1="31" x2="22" y2="36"/><line x1="6" y1="20" x2="11" y2="20"/><line x1="33" y1="20" x2="38" y2="20"/><line x1="11" y1="9" x2="14" y2="12"/><line x1="30" y1="28" x2="33" y2="31"/><line x1="33" y1="9" x2="30" y2="12"/><line x1="11" y1="31" x2="14" y2="28"/></g><path d="M34 42 A12 12 0 0 1 54 40"/><path d="M54 48 A12 12 0 0 1 36 52"/><path d="M50 34 L54 40 L48 42"/><path d="M40 58 L36 52 L42 50"/></svg>
    <svg class="nav-icon" style="left:411px" viewBox="0 0 60 60" stroke="var(--black)" stroke-width="5" stroke-linecap="round"><line x1="30" y1="12" x2="30" y2="48"/><line x1="12" y1="30" x2="48" y2="30"/></svg>
    <svg class="nav-icon" style="left:622px" viewBox="0 0 60 60" fill="none" stroke="var(--black)" stroke-width="6" stroke-linecap="round"><circle cx="24" cy="24" r="14"/><line x1="35" y1="35" x2="52" y2="52"/></svg>
    <svg class="nav-icon" style="left:838px;width:72px;height:64px;top:72px" viewBox="0 0 72 64" fill="none" stroke="var(--black)" stroke-width="5" stroke-linejoin="round"><path d="M36 6 C55 6 68 16 68 30 C68 44 55 54 36 54 C31 54 27 53 23 52 L8 60 L12 46 C7 42 4 36 4 30 C4 16 17 6 36 6 Z"/></svg>
    <div class="nav-avatar" role="img" aria-label="User profile"></div>
    <div class="nav-alert"></div>
  </nav>
</main>
</body>
</html>
```